Menu Board 1000mmx500mm re-design

I would like to re-design exiting menu board 1000mmx500mm. Current board letters are bit to small to read. I would like to have pictures (attached) of the food offered on it and at the same time to create balance between pictures and size of the text to be easily readable. Fonts and colours are up to designer choice but prefer warm and bright colours rather anything dark.

Target Market(s)

Food industry

Industry/Entity Type

Food

Font styles to use
Other font styles liked:
• I leave font choice to designer

Colors
FFC000
F8CF3A
FAE287
FDF2CF
FEFAEE
F0912C
F2A743
F7CA91
FBE8D2
FDF5EE
EE7325
F08F49
F5BC92
FAE3D3
FDF4ED

Requirements
Must have
• Pictures + Text
Nice to have
• Balance between images and text.
Should not have
• Can't think of any

```html
<!DOCTYPE html>
<html lang="en">
<head>
<meta charset="utf-8">
<title>Menu Board</title>
<link href="https://fonts.googleapis.com/css2?family=Rye&family=Lobster&display=swap" rel="stylesheet">
<style>
  :root {
    --wood-light: #c48c55;
    --wood-mid: #b07843;
    --wood-dark: #8e5a2e;
    --band: #9c6738;
    --band-line: #e8c58d;
    --parchment-light: #fbe8c8;
    --parchment: #f4d7a6;
    --parchment-edge: #e2b57a;
    --heading-red: #8a2b2b;
    --ink: #24160c;
    --title-cream: #f3dcae;
    --title-shadow: #6b3f1c;
    --star: #e6c28a;
    --photo-chicken: #d9a85a;
    --photo-bread: #b7864a;
    --photo-wrap: #b9a26a;
    --photo-beet: #8e2f3a;
    --photo-potato: #d8a246;
  }
  * { margin: 0; padding: 0; box-sizing: border-box; }
  html, body { width: 1200px; height: 2400px; overflow: hidden; }
  body {
    position: relative;
    background: linear-gradient(180deg, var(--wood-light) 0%, var(--wood-mid) 55%, var(--wood-light) 100%);
    font-family: "Lobster", cursive;
    color: var(--ink);
  }
  .header-band {
    position: absolute; left: 0; top: 0; width: 1200px; height: 136px;
    background: linear-gradient(180deg, var(--band) 0%, var(--wood-dark) 100%);
  }
  .header-rule {
    position: absolute; left: 0; top: 138px; width: 1200px; height: 6px;
    background: var(--band-line);
    box-shadow: 0 3px 4px rgba(60,30,10,.45);
  }
  .menu-title {
    position: absolute; left: 0; top: 8px; width: 1200px; text-align: center;
    font-family: "Rye", serif; font-size: 100px; line-height: 120px;
    color: var(--title-cream); letter-spacing: 4px;
    text-shadow: 3px 4px 0 var(--title-shadow);
  }
  .star {
    position: absolute; top: 22px; width: 88px; height: 88px;
    background: var(--star); border-radius: 50%; opacity: .85;
  }
  .card {
    position: absolute;
    background: linear-gradient(160deg, var(--parchment-light) 0%, var(--parchment) 60%, var(--parchment-edge) 100%);
    box-shadow: 3px 5px 10px rgba(60,30,10,.4);
    border-radius: 6px;
    display: flex; flex-direction: column; justify-content: center; align-items: center;
    text-align: center;
  }
  .card-title {
    font-family: "Rye", serif; font-size: 44px; line-height: 1.2;
    color: var(--heading-red);
  }
  .card-text { font-size: 41px; line-height: 61px; }
  .price {
    position: absolute;
    background: linear-gradient(160deg, var(--parchment-light), var(--parchment-edge));
    border: 3px solid var(--parchment-edge);
    box-shadow: 2px 4px 6px rgba(60,30,10,.4);
    border-radius: 4px;
    display: flex; justify-content: center; align-items: center;
    font-family: "Rye", serif; font-size: 38px; color: var(--heading-red);
  }
  .photo { position: absolute; box-shadow: 4px 8px 14px rgba(50,25,8,.45); }
  .photo-chicken { left: 664px; top: 237px; width: 488px; height: 403px; border-radius: 40% 30% 45% 35%; background: radial-gradient(circle at 40% 45%, var(--photo-chicken), #8a5a2c); }
  .photo-ciabatta { left: 83px; top: 712px; width: 469px; height: 288px; border-radius: 50% 45% 48% 40%; background: radial-gradient(ellipse at 50% 40%, #d9a866, var(--photo-bread) 55%, #6e4520); }
  .photo-wrap { left: 608px; top: 1088px; width: 557px; height: 248px; border-radius: 45% 40% 48% 42%; background: radial-gradient(ellipse at 45% 40%, #e6d6a8, var(--photo-wrap) 55%, #7a4b24); }
  .photo-beetroot { left: 64px; top: 1416px; width: 464px; height: 328px; border-radius: 40%; background: radial-gradient(ellipse at 50% 50%, #c98a7a, var(--photo-beet) 60%, #5e1d28); }
  .photo-potatoes { left: 744px; top: 1768px; width: 405px; height: 280px; border-radius: 45%; background: radial-gradient(ellipse at 50% 45%, #f0c870, var(--photo-potato) 55%, #5b3a22); }
  .sauces .card-title { font-size: 44px; margin-bottom: 10px; }
  .sauces .card-text { font-size: 31px; line-height: 46px; font-style: italic; }
</style>
</head>
<body>
  <div class="header-band"></div>
  <div class="star" style="left:52px" role="img" aria-label="Wooden star ornament"></div>
  <div class="star" style="left:241px" role="img" aria-label="Wooden star ornament"></div>
  <div class="star" style="left:860px" role="img" aria-label="Wooden star ornament"></div>
  <div class="star" style="left:1044px" role="img" aria-label="Wooden star ornament"></div>
  <h1 class="menu-title">MENU</h1>
  <div class="header-rule"></div>

  <section class="card" style="left:19px;top:176px;width:586px;height:243px">
    <h2 class="card-title">1/4 CHICKEN BOX</h2>
    <p class="card-text">Roti Chicken,<br>Veggie &amp; Salad</p>
  </section>
  <div class="price" style="left:539px;top:277px;width:98px;height:112px">£9</div>

  <section class="card" style="left:24px;top:445px;width:584px;height:243px">
    <h2 class="card-title">1/2 CHICKEN BOX</h2>
    <p class="card-text">Roti Chicken,<br>Veggie &amp; Salad</p>
  </section>
  <div class="price" style="left:539px;top:544px;width:98px;height:109px">£14</div>

  <div class="photo photo-chicken" role="img" aria-label="Photo of roast chicken quarter with vegetable rice on a wooden plate"></div>

  <div class="photo photo-ciabatta" role="img" aria-label="Photo of chicken ciabatta with rocket on a wooden board"></div>
  <section class="card" style="left:608px;top:723px;width:547px;height:296px;padding-left:30px">
    <h2 class="card-title">CIABATTA</h2>
    <p class="card-text">Roti Chicken, Rucola,<br>Caramelized Onions,<br>Tomato, Fresh Onion</p>
  </section>
  <div class="price" style="left:579px;top:819px;width:101px;height:112px">£6</div>

  <section class="card" style="left:29px;top:1040px;width:544px;height:355px;padding-right:10px">
    <h2 class="card-title">WRAP</h2>
    <p class="card-text">Roti Chicken, Crunchy<br>Slaw, Tomato,<br>Fresh Onion<br>&amp; Sauce of your choice</p>
  </section>
  <div class="price" style="left:496px;top:1187px;width:99px;height:109px">£7</div>
  <div class="photo photo-wrap" role="img" aria-label="Photo of grilled chicken wrap with slaw on a wooden board"></div>

  <div class="photo photo-beetroot" role="img" aria-label="Photo of beetroot wrap halves filled with chicken and greens"></div>
  <section class="card" style="left:528px;top:1421px;width:627px;height:326px;padding-left:30px">
    <h2 class="card-title">BEETROOT WRAP</h2>
    <p class="card-text">Roti Chicken, Crunchy Slaw,<br>Tomato, Fresh Onion<br>&amp; Sauce of your choice</p>
  </section>
  <div class="price" style="left:517px;top:1592px;width:99px;height:112px">£8</div>

  <section class="card" style="left:16px;top:1779px;width:696px;height:218px;padding-right:40px">
    <h2 class="card-title">ROASTED POTATOES</h2>
    <p class="card-text">Thyme &amp; Garlic</p>
  </section>
  <div class="price" style="left:600px;top:1901px;width:136px;height:109px">£2,5</div>
  <div class="photo photo-potatoes" role="img" aria-label="Photo of roasted potatoes with thyme"></div>

  <section class="card" style="left:35px;top:2072px;width:357px;height:117px">
    <h2 class="card-title">WATER</h2>
  </section>
  <div class="price" style="left:413px;top:2072px;width:99px;height:112px">£1</div>

  <section class="card" style="left:29px;top:2213px;width:547px;height:147px">
    <h2 class="card-title">CAN &amp; JUICES</h2>
  </section>
  <div class="price" style="left:589px;top:2216px;width:128px;height:112px">£1,8</div>

  <section class="card sauces" style="left:725px;top:2074px;width:430px;height:296px">
    <h2 class="card-title">SAUCES</h2>
    <p class="card-text">Signature BBQ PiriPiri<br>Sweet Chilli Garlic Mayo</p>
  </section>
</body>
</html>
```